Business Card & Email Signature Design || Upmarket + Luxury

Rima Vale Honey, a New Zealand Manuka Honey company needs a Business Card & Email Signature design.

Our logo's are attached in Gold & Black versions, feel free to be creative with how you use the logo and it's patterns in your design.

Style:
- Looking for an Elegant, Luxurious, Upmarket feel.
- Black/Matte Black Card, Gold Foil, UV Embossing

Information to Add:

- Logo
- Company Name: Rima Vale Honey
- Name: Martin Delrow
- Title: Creative Director
- Phone: +64 2815 90 617
- Email: martin@rimavalehoney.example.nz
- Website: www.rimavalehoney.example.nz

- Socials: ***For email Signature Only***
- Facebook: https://www.facebook.com/rimavalehoney/
- Instagram: https://www.instagram.com/rimavalehoney/

Target Market(s)

Asia/Europe Luxury, Upmarket

Contact Information for Business Card

- Logo
- Name: Martin Delrow
- Phone: +64 2815 90 617

Font styles to use
Other font styles liked:
• Champagne & Limousines (Attached)

Requirements
Must have
• Business Card & Email Signature Design.

Looking for a Sleek, Luxury, Upmarket Design.

```html
<!DOCTYPE html>
<html lang="en">
<head>
<meta charset="utf-8">
<title>Rima Vale Honey Co. — Business Card &amp; Email Signature</title>
<link href="https://fonts.googleapis.com/css2?family=Jost:wght@300;400;500&display=swap" rel="stylesheet">
<style>
  :root {
    --stage: #e6e6e6;
    --paper: #ffffff;
    --matte-black: #0b0506;
    --gold-foil: #d9c27a;
    --gold-light: #efe6a4;
    --gold-mid: #e8d8a8;
    --gold-deep: #c9a86a;
    --ink: #3a3a3a;
    --ink-dark: #1e1e1e;
    --ink-soft: #4a4a4a;
  }
  * { margin: 0; padding: 0; box-sizing: border-box; }
  html, body { width: 1200px; height: 916px; overflow: hidden; }
  body {
    position: relative;
    background: var(--paper);
    font-family: "Jost", "Futura", sans-serif;
    font-weight: 300;
  }

  /* Card presentation area */
  .card-stage {
    position: absolute; left: 0; top: 0;
    width: 1200px; height: 573px;
    background: var(--stage);
  }
  .card {
    position: absolute; top: 152px;
    width: 406px; height: 245px;
    overflow: hidden;
  }
  .card--front { left: 134px; background: var(--matte-black); color: var(--gold-foil); }
  .card--back {
    left: 636px; color: var(--ink);
    background: linear-gradient(120deg, var(--gold-light) 0%, var(--gold-mid) 40%, var(--gold-deep) 100%);
  }

  /* Plain hairline rule through the mark position */
  .rule { position: absolute; left: 0; height: 1px; }
  .card .rule { top: 70px; width: 406px; }
  .card--front .rule { background: var(--gold-foil); opacity: 0.8; }
  .card--back .rule { background: var(--ink); opacity: 0.55; }

  .mark-spot { position: absolute; border-radius: 50%; }
  .card .mark-spot { left: 183px; top: 50px; width: 40px; height: 40px; }
  .card--front .mark-spot { background: var(--matte-black); border: 1px solid var(--gold-foil); }
  .card--back .mark-spot { background: var(--gold-mid); border: 1px solid var(--ink); }

  .centered {
    position: absolute; left: 0; width: 100%;
    text-align: center; white-space: nowrap; line-height: 1;
  }
  .wordmark { font-weight: 400; text-transform: uppercase; letter-spacing: 0.16em; }
  .card .wordmark { top: 132px; font-size: 26px; }
  .card .wordmark-suffix { top: 161px; font-size: 10px; letter-spacing: 0.1em; font-weight: 400; }
  .card .website { top: 207px; font-size: 14px; letter-spacing: 0.04em; }

  .person-name { font-weight: 400; text-transform: uppercase; letter-spacing: 0.2em; }
  .card .person-name { top: 131px; font-size: 28px; }
  .role { font-weight: 500; text-transform: uppercase; letter-spacing: 0.2em; }
  .card .role { top: 159px; font-size: 12px; }
  .card .phone { top: 182px; font-size: 17px; letter-spacing: 0.05em; }
  .card .email { top: 205px; font-size: 15px; letter-spacing: 0.03em; }

  /* Email signature */
  .signature { position: absolute; left: 0; top: 573px; width: 1200px; height: 343px; color: var(--ink); }
  .signature .rule {
    left: 192px; top: 145px; width: 552px;
    background: linear-gradient(90deg, rgba(58,58,58,0) 0%, rgba(58,58,58,0.85) 55%, rgba(58,58,58,0) 100%);
  }
  .signature .mark-spot {
    left: 289px; top: 114px; width: 60px; height: 60px;
    background: var(--paper); border: 1px solid var(--ink);
  }
  .signature .brand {
    position: absolute; left: 160px; top: 211px; width: 330px;
    text-align: center; white-space: nowrap; line-height: 1;
  }
  .signature .wordmark { display: block; font-size: 24px; }
  .signature .wordmark-suffix { display: block; font-size: 10px; font-weight: 400; letter-spacing: 0.1em; margin-top: 4px; }

  .signature .contact { position: absolute; left: 464px; top: 76px; }
  .signature .person-name { font-size: 33px; line-height: 1; letter-spacing: 0.17em; color: var(--ink-dark); }
  .signature .role { font-size: 14px; line-height: 1; margin-top: 5px; color: var(--ink-soft); }
  .signature .contact-lines { margin-top: 28px; font-size: 19px; line-height: 26px; letter-spacing: 0.04em; }
  .social { display: flex; align-items: center; gap: 4px; font-weight: 400; }
  .social-dot { width: 17px; height: 17px; border: 1.5px solid var(--ink); border-radius: 50%; }
  .contact-lines a { color: inherit; text-decoration: none; }
</style>
</head>
<body>
  <section class="card-stage">
    <article class="card card--front">
      <div class="rule"></div>
      <div class="mark-spot"></div>
      <div class="centered wordmark">Rima Vale Honey</div>
      <div class="centered wordmark-suffix">CO.</div>
      <div class="centered website">www.rimavalehoney.example.nz</div>
    </article>

    <article class="card card--back">
      <div class="rule"></div>
      <div class="mark-spot"></div>
      <div class="centered person-name">Martin Delrow</div>
      <div class="centered role">Creative Director</div>
      <div class="centered phone">+64 2815 90 617</div>
      <div class="centered email">martin@rimavalehoney.example.nz</div>
    </article>
  </section>

  <section class="signature">
    <div class="rule"></div>
    <div class="mark-spot"></div>
    <div class="brand">
      <span class="wordmark">Rima Vale Honey</span>
      <span class="wordmark-suffix">CO.</span>
    </div>
    <div class="contact">
      <div class="person-name">Martin Delrow</div>
      <div class="role">Creative Director</div>
      <div class="contact-lines">
        <div class="phone">+64 2815 90 617</div>
        <div class="email">martin@rimavalehoney.example.nz</div>
        <a class="social" href="https://www.facebook.com/rimavalehoney/"><span class="social-dot"></span>/rimavalehoney</a>
        <a class="social" href="https://www.instagram.com/rimavalehoney/"><span class="social-dot"></span>/rimavalehoney</a>
      </div>
    </div>
  </section>
</body>
</html>
```